contemporary upscale hair salon

we need a business card design for a modern upscale salon. I would like the card to be vertical, simple, and easy to read. I would like a black matte finish on the info side with white on the back of the card, white lettering with a splash of red incorporated somewhere in there. I also want to incorporate embossing and/or cut out in the letters. The info I would like; Name of the business (Vessa Salon) stylist name (Joan) phone number(5093146620) and web address (www.vessasalon-example.com) I am open to putting shears on the card but without it looking too cheap. Looking for something really modern and edgy. these are just ideas I have, but feel free to show me your creative ideas.
please note: the website is still under construction please do not use any images or colors off the web page. Also i currently do not have a logo, that will be a future project.

```html
<!DOCTYPE html>
<html lang="en">
<head>
<meta charset="utf-8">
<title>Vessa Salon – Business Card</title>
<link rel="stylesheet" href="https://fonts.googleapis.com/css2?family=Oswald:wght@300;400;500&display=swap">
<style>
  :root {
    --backdrop: #e6e6e6;
    --card-white: #f7f7f7;
    --card-black: #141414;
    --accent: #e2195f;
    --ink: #3a3a3a;
    --ink-soft: #6b6b6b;
    --light: #f2f2f2;
  }
  * { margin: 0; padding: 0; box-sizing: border-box; }
  html, body {
    width: 1200px;
    height: 800px;
    overflow: hidden;
    background: var(--backdrop);
    font-family: "Oswald", "Arial Narrow", sans-serif;
  }
  .stage {
    position: relative;
    width: 1200px;
    height: 800px;
  }
  .card {
    position: absolute;
    top: 138px;
    width: 300px;
    height: 524px;
    border-radius: 3px;
    box-shadow: 0 10px 28px rgba(0,0,0,0.18);
  }
  .card--info {
    left: 250px;
    background: var(--card-white);
    padding: 54px 0 0 40px;
  }
  .card--brand {
    left: 650px;
    background: var(--card-black);
    display: flex;
    flex-direction: column;
    align-items: center;
    padding-top: 150px;
  }
  .business-name {
    font-weight: 400;
    font-size: 36px;
    line-height: 1;
    letter-spacing: 0.5px;
  }
  .card--info .business-name { color: var(--accent); }
  .card--brand .business-name { color: var(--light); margin-top: 22px; font-size: 40px; }
  .brand-dot {
    width: 56px;
    height: 56px;
    border-radius: 50%;
    background: var(--accent);
  }
  .stylist {
    margin-top: 18px;
    font-size: 20px;
    font-weight: 300;
    color: var(--ink-soft);
  }
  .stylist .stylist-name { color: var(--accent); font-weight: 400; }
  .contact-list {
    list-style: none;
    margin-top: 10px;
  }
  .contact-item {
    display: flex;
    align-items: center;
    gap: 8px;
    font-size: 17px;
    font-weight: 300;
    line-height: 26px;
    color: var(--ink);
  }
  .contact-item--web { color: var(--accent); }
  .contact-icon { width: 16px; height: 16px; flex: none; }
</style>
</head>
<body>
<main class="stage">
  <section class="card card--info" aria-label="Card information side">
    <h1 class="business-name">Vessa Salon</h1>
    <p class="stylist"><span class="stylist-name">Joan</span> Stylist</p>
    <ul class="contact-list">
      <li class="contact-item contact-item--phone">
        <svg class="contact-icon" viewBox="0 0 16 16" aria-hidden="true">
          <path d="M4 1.5c.6 0 1 .4 1.2 1l.8 2.3c.2.5 0 1-.4 1.3L4.5 7c.9 1.9 2.6 3.6 4.5 4.5l.9-1.1c.3-.4.8-.6 1.3-.4l2.3.8c.6.2 1 .6 1 1.2V14c0 .6-.5 1-1.1 1C7.2 14.6 1.4 8.8 1 2.6 1 2 1.4 1.5 2 1.5z" fill="var(--accent)"/>
        </svg>
        509 314 6620
      </li>
      <li class="contact-item contact-item--web">
        <svg class="contact-icon" viewBox="0 0 16 16" aria-hidden="true">
          <circle cx="8" cy="8" r="8" fill="var(--accent)"/>
          <rect x="7" y="7" width="2" height="5" fill="#fff"/>
          <circle cx="8" cy="4.6" r="1.1" fill="#fff"/>
        </svg>
        www.vessasalon-example.com
      </li>
    </ul>
  </section>

  <section class="card card--brand" aria-label="Card brand side">
    <span class="brand-dot" aria-hidden="true"></span>
    <p class="business-name">Vessa Salon</p>
  </section>
</main>
</body>
</html>
```